Marlow Research, Inc. Site Design Project

Marlow Research, Inc is my private and small research office.
This naming shows:
We investigate every(*: asterisk) issue to support society.
We investigate "a star risk" which means every critical things for example, information security, branding, public communication - to understand for our clients - especially innovative person.
Last year, we had faced the great disaster in Japan, we investigated the damaged place, schools, and local governments, and supported communities like Quillfest Ogura.
So I want to get a high concept sites with good logo and to use card, website, and our letter.
Reason: We would like to look for more competitive candidates.
I uploaded the latest logo. If you have any idea to adapt it to your design, I appreciate it.
* marketing section of leading companies(enterprises)
* promotion agencies of government
* futurist and researcher
* business managers
Communication
for desirable future

```html
<!DOCTYPE html>
<html lang="en">
<head>
<meta charset="utf-8">
<title>Marlow Research, Inc.</title>
<link rel="stylesheet" href="https://fonts.googleapis.com/css2?family=Arimo:wght@400;700&family=Jura:wght@400;500;600&display=swap">
<style>
  :root {
    --red: #e8141b;
    --red-deep: #c80f14;
    --ink: #1c1c1c;
    --grey: #6b6b6b;
    --grey-light: #9a9a9a;
    --frame: #0d0d0d;
    --panel: #ebe9e5;
    --white: #ffffff;
  }
  * { box-sizing: border-box; margin: 0; padding: 0; }
  html, body { width: 1200px; height: 962px; overflow: hidden; background: var(--white); }
  body { position: relative; font-family: "Arimo", Arial, sans-serif; color: var(--grey); }

  .brand {
    position: absolute; left: 60px; top: 38px;
    font-family: "Jura", sans-serif; font-weight: 500; font-size: 40px;
    color: var(--ink); letter-spacing: 1px;
  }
  .helpline { position: absolute; right: 95px; top: 14px; text-align: right; font-family: "Jura", sans-serif; }
  .helpline-label { display: flex; align-items: center; justify-content: flex-end; gap: 2px; font-size: 23px; color: var(--grey); }
  .helpline-number { font-size: 23px; color: var(--red); margin-top: 4px; letter-spacing: 1px; }

  .members-mail { position: absolute; left: 570px; top: 110px; width: 76px; text-align: center; font-size: 12px; color: var(--red-deep); }
  .members-mail svg { display: block; margin: 0 auto 3px; }

  .tagline {
    position: absolute; left: 143px; top: 159px;
    font-size: 15px; letter-spacing: 3.2px; color: var(--red);
  }
  .main-nav {
    position: absolute; left: 540px; top: 153px; width: 570px; height: 28px;
    background: var(--red); border-radius: 6px 6px 0 0;
    display: flex; align-items: center; padding-left: 47px;
    font-size: 14px; font-weight: 700; color: var(--white);
  }
  .main-nav span { white-space: pre; }

  .slider { position: absolute; left: 60px; top: 180px; width: 1081px; height: 410px; }
  .slider-frame { position: absolute; inset: 0; }
  .slide-photo {
    position: absolute; left: 12px; top: 12px; width: 1058px; height: 350px;
    background: linear-gradient(90deg, #c9a48c 0%, #d9bba8 22%, #e6e2dc 42%, var(--panel) 60%);
  }
  .slide-text { position: absolute; left: 485px; top: 155px; font-family: "Jura", sans-serif; }
  .slide-title { font-size: 46px; font-weight: 500; color: var(--ink); letter-spacing: -0.5px; }
  .slide-sub { font-size: 22px; color: var(--red); margin-top: -4px; }
  .slide-dots { position: absolute; left: 500px; top: 375px; display: flex; gap: 17px; }
  .slide-dots i { width: 18px; height: 18px; border-radius: 50%; background: #a8a8a8; display: block; }
  .slide-dots i.active { background: #8a1010; }
  .slider-shadow {
    position: absolute; left: 100px; top: 572px; width: 1000px; height: 48px;
    background: radial-gradient(ellipse at 50% 20%, rgba(0,0,0,.35), rgba(0,0,0,0) 70%);
  }

  .columns { position: absolute; left: 70px; top: 625px; width: 1070px; height: 270px; display: flex; }
  .column { width: 25%; padding: 8px 26px 0; border-right: 1px solid #ececec; }
  .column:last-child { border-right: none; }
  .column h2 { font-family: "Jura", sans-serif; font-weight: 500; font-size: 21px; color: var(--red); text-align: center; margin-bottom: 18px; }
  .about p { font-size: 12.5px; line-height: 16px; text-align: justify; }
  .services ul { list-style: none; font-size: 12.5px; line-height: 18px; padding-left: 10px; }
  .testimonial { font-size: 12.5px; line-height: 16px; text-align: justify; }
  .testimonial-photo {
    float: left; width: 77px; height: 97px; margin: 0 6px 4px 0;
    background: linear-gradient(180deg, #d6dde4, #3b3f48); border: 1px solid var(--red);
  }
  .testimonial-author { clear: both; text-align: right; color: var(--red-deep); font-weight: 700; font-size: 12.5px; line-height: 16px; margin-top: 12px; }
  .join { text-align: center; }
  .social { display: flex; justify-content: center; gap: 3px; margin-top: 20px; }
  .social span {
    width: 42px; height: 42px; border-radius: 50%; background: var(--red);
    color: var(--white); font-size: 10px; font-weight: 700; display: flex; align-items: center; justify-content: center;
  }
  .contact-lines { margin-top: 66px; font-size: 12.5px; line-height: 16px; }
  .contact-lines b { color: var(--red-deep); font-weight: 400; }

  .site-footer { position: absolute; left: 40px; top: 896px; width: 1115px; height: 66px; }
  .footer-links { position: absolute; left: 0; right: 0; top: 14px; text-align: center; font-size: 14px; color: var(--white); white-space: pre; }
  .copyright { position: absolute; left: 0; right: 0; top: 44px; text-align: center; font-size: 12px; color: #2a0000; }
</style>
</head>
<body>
  <header>
    <div class="brand">Marlow Research, Inc.</div>
    <div class="helpline">
      <div class="helpline-label">
        <svg width="28" height="28" viewBox="0 0 24 24" aria-hidden="true"><path fill="#6b6b6b" d="M6.6 10.8a15 15 0 0 0 6.6 6.6l2.2-2.2a1 1 0 0 1 1-.25 11.4 11.4 0 0 0 3.6.57 1 1 0 0 1 1 1V20a1 1 0 0 1-1 1A17 17 0 0 1 3 4a1 1 0 0 1 1-1h3.5a1 1 0 0 1 1 1c0 1.25.2 2.45.57 3.57a1 1 0 0 1-.25 1z"/></svg>
        HELPLINE
      </div>
      <div class="helpline-number">+1-800-555-0142</div>
    </div>
    <div class="members-mail">
      <svg width="26" height="24" viewBox="0 0 26 24" aria-hidden="true"><rect x="1" y="3" width="24" height="19" rx="3" fill="#e4e4e4" stroke="#b5b5b5"/><text x="13" y="17" text-anchor="middle" font-size="11" font-family="Arial" fill="#555">@</text></svg>
      Members Mail
    </div>
    <div class="tagline">CUSTOMER SERVICE &amp; SATISFACTION</div>
    <nav class="main-nav"><span>About Us    |    Services    |    Career    |    Query    |   Feedback    |    Contact</span></nav>
  </header>

  <section class="slider">
    <svg class="slider-frame" width="1081" height="410" viewBox="0 0 1081 410" aria-hidden="true">
      <path d="M22 0 H1059 Q1081 0 1081 22 V380 Q1081 392 1066 394 Q540 420 15 394 Q0 392 0 380 V22 Q0 0 22 0 Z" fill="#0d0d0d"/>
    </svg>
    <div class="slide-photo" role="img" aria-label="Photo of a customer service agent wearing a headset and speaking on the phone"></div>
    <div class="slide-text">
      <div class="slide-title">Leadership experience</div>
      <div class="slide-sub">in customer interaction management</div>
    </div>
    <div class="slide-dots"><i class="active"></i><i></i><i></i></div>
  </section>
  <div class="slider-shadow"></div>

  <main class="columns">
    <section class="column about">
      <h2>Little About Hello</h2>
      <p>We investigate "a star risk" which means every critical things for example, information security, branding, public communication - to understand for our clients - especially innovative person. Last year, we had faced the great disaster in Japan, we investigated the damaged place, schools, and local governments, and supported communities like Quillfest Ogura.</p>
    </section>
    <section class="column services">
      <h2>Services Offered</h2>
      <ul>
        <li>Marketing section of leading companies(enterprises)</li>
        <li>Promotion agencies of government</li>
        <li>Futurist and researcher</li>
        <li>Business managers</li>
        <li>Marketing section of leading companies(enterprises)</li>
        <li>Promotion agencies of government</li>
        <li>Futurist and researcher</li>
        <li>Business managers</li>
      </ul>
    </section>
    <section class="column testimonial-col">
      <h2>Testimonials</h2>
      <div class="testimonial">
        <div class="testimonial-photo" role="img" aria-label="Portrait photo of the client giving the testimonial"></div>
        With over two decades of leadership experience in customer interaction management, some of the biggest names in business trust Northwind to tir With over two decades of leadership experience in customer interaction man
      </div>
      <div class="testimonial-author">Mr. Daniel Verhoeven<br>CEO, KESTRELTEK</div>
    </section>
    <section class="column join">
      <h2>Join us</h2>
      <div class="social"><span>Post</span><span>Share</span><span>Plus</span></div>
      <div class="contact-lines">
        <b>Call us :</b> +1 - 555 0198 4471<br>
        <b>Email us :</b> info@marlowresearch.example
      </div>
    </section>
  </main>

  <footer class="site-footer">
    <svg width="1115" height="66" viewBox="0 0 1115 66" aria-hidden="true" style="position:absolute;inset:0">
      <path d="M10 66 L28 10 Q32 0 48 0 H1067 Q1083 0 1087 10 L1105 66 Z" fill="#c9c9c9"/>
      <path d="M20 66 L36 12 Q40 4 54 4 H1061 Q1075 4 1079 12 L1095 66 Z" fill="#e8141b"/>
    </svg>
    <div class="footer-links">About Us    |    Services    |    Query    |  Feedback    |    Contact</div>
    <div class="copyright">©  2012, All Rights Reserved.</div>
  </footer>
</body>
</html>
```